I have a new startup... www.hirewithplindle.com
An issue Im running into is when people create profiles there banner images are getting messed up. So instead I would like anywhere to 10-15 banners created as stock banners for my site the people signing up need to choose from so the website looks more in uniform. The site contains graphic designers, photographers, & videographers so maybe some banners can be patterns of a camera outline or graphic design tools etc. Need really clean and sleek looking banners that these people can pick from that will make sense.
I will attach my logo if you want to do a cool "Plindle" pattern design as a banner.
Banner sizes 2000px by 560px.

If you have any questions please let me know.

```html
<!DOCTYPE html>
<html lang="en">
<head>
<meta charset="utf-8">
<title>Plindle — Stock Profile Banners</title>
<link rel="stylesheet" href="https://fonts.googleapis.com/css2?family=Montserrat:wght@600;700;800&display=swap">
<style>
  :root {
    --board: #444444;
    --brand: #c94a2a;
    --navy-deep: #050b24;
    --navy-glow: #13284a;
    --slate: #8a8a8a;
    --charcoal: #120f0f;
    --paper: #ffffff;
    --ink: #222222;
    --white: #ffffff;
    --olive: #4d4a2a;
    --sun: #f2dc18;
  }
  * { margin: 0; padding: 0; box-sizing: border-box; }
  html, body { width: 1021px; height: 1200px; overflow: hidden; background: var(--board); }
  body { position: relative; font-family: "Montserrat", Arial, sans-serif; }
  .banner { position: absolute; left: 25.5px; width: 970px; height: 271px; display: block; }
  .banner--night { top: 18.5px; }
  .banner--slate { top: 308px; }
  .banner--studio { top: 597px; }
  .banner--clean { top: 887px; }
  .wordmark { font-family: "Montserrat", Arial, sans-serif; font-weight: 800; fill: var(--brand); }
  .headline { font-family: "Montserrat", Arial, sans-serif; font-weight: 600; }
  .tagline { font-family: "Montserrat", Arial, sans-serif; font-weight: 600; font-size: 12px; }
  .on-dark { fill: var(--white); }
  .on-light { fill: var(--ink); }
  .frame-line { fill: none; stroke: var(--brand); stroke-width: 1.2; }
</style>
</head>
<body>

<!-- Banner: night camera -->
<svg class="banner banner--night" viewBox="0 0 970 271" xmlns="http://www.w3.org/2000/svg">
  <defs>
    <radialGradient id="nightSky" cx="0.35" cy="0.1" r="0.9">
      <stop offset="0" stop-color="var(--navy-glow)"/>
      <stop offset="1" stop-color="var(--navy-deep)"/>
    </radialGradient>
    <radialGradient id="neonCamera" cx="0.6" cy="0.55" r="0.6">
      <stop offset="0" stop-color="#3aa0d8"/>
      <stop offset="0.55" stop-color="#5a3a8c"/>
      <stop offset="1" stop-color="#0a1230" stop-opacity="0.2"/>
    </radialGradient>
  </defs>
  <rect width="970" height="271" fill="url(#nightSky)"/>
  <rect x="9" y="16" width="360" height="240" rx="30" fill="url(#neonCamera)" opacity="0.55" role="img" aria-label="Colourful neon line illustration of a DSLR camera"/>
  <rect x="825" y="19" width="125" height="232" rx="60" fill="var(--olive)" opacity="0.7" role="img" aria-label="Faint light bulb shape filled with creative tool icons"/>
  <text class="wordmark" x="616" y="94" font-size="78" text-anchor="middle" textLength="304" lengthAdjust="spacingAndGlyphs">PLINDLE</text>
  <text class="headline on-dark" x="616" y="162" font-size="36" text-anchor="middle" textLength="379" lengthAdjust="spacingAndGlyphs">FIND CREATIVE PROS</text>
  <text class="tagline on-dark" x="616" y="194" text-anchor="middle" textLength="392" lengthAdjust="spacingAndGlyphs">GRAPHIC DESIGNERS , PHOTOGRAPHERS, &amp; VIDEOGRAPHERS</text>
</svg>

<!-- Banner: slate watercolour -->
<svg class="banner banner--slate" viewBox="0 0 970 271" xmlns="http://www.w3.org/2000/svg">
  <defs>
    <radialGradient id="watercolour" cx="0.55" cy="0.5" r="0.6">
      <stop offset="0" stop-color="#3a5f8a"/>
      <stop offset="0.5" stop-color="#5c6a78"/>
      <stop offset="1" stop-color="var(--slate)"/>
    </radialGradient>
  </defs>
  <rect width="970" height="271" fill="var(--slate)"/>
  <rect x="35" y="16" width="142" height="238" rx="65" fill="var(--sun)" role="img" aria-label="Yellow light bulb shape filled with design and photo tool icons"/>
  <rect x="623" y="0" width="347" height="271" fill="url(#watercolour)" role="img" aria-label="Ink and watercolour illustration of a photographer holding a camera"/>
  <text class="wordmark" x="413" y="73" font-size="78" text-anchor="middle" textLength="304" lengthAdjust="spacingAndGlyphs">PLINDLE</text>
  <text class="headline on-dark" x="413" y="142" font-size="36" text-anchor="middle" textLength="378" lengthAdjust="spacingAndGlyphs">FIND CREATIVE PROS</text>
  <text class="tagline on-dark" x="413" y="173" text-anchor="middle" textLength="392" lengthAdjust="spacingAndGlyphs">GRAPHIC DESIGNERS , PHOTOGRAPHERS, &amp; VIDEOGRAPHERS</text>
</svg>

<!-- Banner: studio desk -->
<svg class="banner banner--studio" viewBox="0 0 970 271" xmlns="http://www.w3.org/2000/svg">
  <defs>
    <radialGradient id="studioDark" cx="0.55" cy="0.5" r="0.6">
      <stop offset="0" stop-color="#231c1b"/>
      <stop offset="1" stop-color="var(--charcoal)"/>
    </radialGradient>
    <linearGradient id="deskTones" x1="0" y1="0" x2="1" y2="1">
      <stop offset="0" stop-color="#d8d6d2"/>
      <stop offset="0.6" stop-color="#bdb8b1"/>
      <stop offset="1" stop-color="#8c7b6c"/>
    </linearGradient>
    <linearGradient id="rigTones" x1="0" y1="0" x2="1" y2="1">
      <stop offset="0" stop-color="#3a302c" stop-opacity="0"/>
      <stop offset="0.6" stop-color="#2a2422"/>
      <stop offset="1" stop-color="#1a1514"/>
    </linearGradient>
  </defs>
  <rect width="970" height="271" fill="url(#studioDark)"/>
  <path d="M0 0 H362 C428 65 436 205 355 271 H0 Z" fill="var(--brand)"/>
  <path d="M0 0 H342 C406 65 414 205 335 271 H0 Z" fill="url(#deskTones)" role="img" aria-label="Top-down photo of a designer working at a desk with a drawing tablet, colour swatches and camera"/>
  <rect x="820" y="0" width="150" height="271" fill="url(#rigTones)" role="img" aria-label="Photo of a hand holding a video camera rig"/>
  <text class="wordmark" x="616" y="94" font-size="78" text-anchor="middle" textLength="304" lengthAdjust="spacingAndGlyphs">PLINDLE</text>
  <text class="headline on-dark" x="616" y="162" font-size="36" text-anchor="middle" textLength="379" lengthAdjust="spacingAndGlyphs">FIND CREATIVE PROS</text>
  <text class="tagline on-dark" x="616" y="194" text-anchor="middle" textLength="392" lengthAdjust="spacingAndGlyphs">GRAPHIC DESIGNERS , PHOTOGRAPHERS, &amp; VIDEOGRAPHERS</text>
</svg>

<!-- Banner: clean white -->
<svg class="banner banner--clean" viewBox="0 0 970 271" xmlns="http://www.w3.org/2000/svg">
  <rect width="970" height="271" fill="var(--paper)"/>
  <path class="frame-line" d="M118 10 H9 V119"/>
  <path class="frame-line" d="M9 155 V264 H118"/>
  <path class="frame-line" d="M846 10 H956 V119"/>
  <path class="frame-line" d="M956 155 V264 H846"/>
  <text class="wordmark" x="97" y="208" font-size="200" textLength="775" lengthAdjust="spacingAndGlyphs">PLINDLE</text>
  <rect x="405" y="10" width="175" height="155" rx="40" fill="#1a1a1a" opacity="0.85" role="img" aria-label="Black line illustration of hands holding a camera"/>
  <text class="headline on-light" x="101" y="251" font-size="33" textLength="378" lengthAdjust="spacingAndGlyphs">FIND CREATIVE PROS</text>
  <text class="tagline on-light" x="494" y="242" font-size="11.5" textLength="390" lengthAdjust="spacingAndGlyphs">GRAPHIC DESIGNERS , PHOTOGRAPHERS, &amp; VIDEOGRAPHERS</text>
</svg>

</body>
</html>
```